Launching a new real estate agency in Monaco

Hello, I am opening a new real estate agency in Monaco. For the purpose of my activity, in order to be known quickly among a fierce competition I need an advertising campaign that will be broadcast in local magazines, newspapers, paper board, etc.

You will find example of pictures of Monaco on which I have the rights and my logo. You can always pick other images that I can buy if the price is reasonable for a commercial use (<200 $)

Please respect the color code.

I wish you good luck and look forward to give you my feedbacks

Reason: Only few projects posted were respecting the brief and of quality. Hoping to receive more in coming days

Target Market(s)

International high-end clientele of all ages, all genders.

Industry/Entity Type

Real Estate Agent

Font styles to use
Serif

Requirements
Must have
• 1/ My logo
• 2/ This message "Un nouveau regard sur l'immobilier" means in English a fresh look at real estate or new eyes on real-estate.
• 3/ My address: 14 rue des Orvilles, Passage Marcellin, 98 000 Monaco
• 4/ Phone number: +377.93.48.25.71
• 5/ Website: www.brunor-agency.com.
• 6/ Format: Files should be easily adjustable but I'd like a vertical display to fit easily in Magazines, Poster and billboard. So please work in high resolution !
Nice to have
• Please think about your design in accordance with the message I want to display.
Should not have
• A simple poster with a picture of Monaco that does not take into consideration the message of the advertisement, "Un nouveau regard sur l'immobilier" which means in english, new eyes on real-estate or a new look at real-estate, or new vision at real-estate.

```html
<!DOCTYPE html>
<html lang="fr">
<head>
<meta charset="utf-8">
<title>Brunor Agency – Un nouveau regard sur l'immobilier</title>
<link href="https://fonts.googleapis.com/css2?family=Questrial&display=swap" rel="stylesheet">
<style>
  :root {
    --navy: #1c2a3d;
    --orange: #f3854a;
    --sand: #e8e3de;
    --gold: #f6b23a;
    --sea: #9a7fb0;
    --copper: #e9b7a0;
  }
  html, body { margin: 0; padding: 0; overflow: hidden; }
  body { width: 927px; height: 1200px; background: var(--sand); }
  .poster {
    position: relative; width: 927px; height: 1200px; overflow: hidden;
    font-family: "Questrial", sans-serif; color: var(--navy);
    background: linear-gradient(180deg, var(--sand) 0px, #ecd9cb 110px, #f2a375 270px, var(--orange) 380px, var(--orange) 400px);
  }
  .top-rule { position: absolute; top: 0; left: 0; width: 927px; height: 6px; background: #111; }
  .side-bar { position: absolute; top: 0; left: 0; width: 26px; height: 396px; background: var(--navy); }
  .headline {
    position: absolute; left: 52px; top: 72px; margin: 0;
    font-weight: 400; font-size: 80px; line-height: 91px; letter-spacing: 1px;
  }
  .photo {
    position: absolute; left: 0; top: 384px; width: 927px; height: 590px;
    background:
      radial-gradient(ellipse 420px 260px at 720px 420px, rgba(240,150,60,.85), rgba(120,60,70,0) 70%),
      linear-gradient(180deg, var(--orange) 0px, #f7a243 40px, var(--gold) 60px, #d98a9a 82px, var(--sea) 150px, #7f6c9c 330px, #3c3d5c 520px, var(--navy) 590px);
  }
  .photo::after {
    content: ""; position: absolute; left: 0; right: 0; top: 0; height: 60px;
    background: linear-gradient(180deg, var(--orange), rgba(243,133,74,0));
  }
  .brand-panel {
    position: absolute; left: 0; top: 960px; width: 634px; height: 240px; background: var(--navy);
    display: flex; align-items: center; justify-content: center; gap: 18px;
  }
  .brand-mark { width: 22px; height: 22px; border-radius: 50%; background: var(--copper); }
  .brand-name { font-size: 44px; letter-spacing: 6px; color: var(--copper); }
  .contact-panel {
    position: absolute; left: 634px; top: 960px; width: 293px; height: 240px; background: var(--orange);
  }
  .contact { position: absolute; left: 27px; top: 56px; font-size: 15px; line-height: 17px; }
  .contact p { margin: 0; }
  .contact .phone { margin-top: 17px; }
  .contact .web { margin-top: 17px; }
</style>
</head>
<body>
<div class="poster">
  <div class="top-rule"></div>
  <div class="side-bar"></div>
  <h1 class="headline">Un nouveau<br>regard sur<br>l'immobilier</h1>
  <div class="photo" role="img" aria-label="Vue aérienne de Monaco au coucher du soleil, mer violette et ville illuminée"></div>
  <div class="brand-panel">
    <span class="brand-mark"></span>
    <span class="brand-name">BRUNOR AGENCY</span>
  </div>
  <div class="contact-panel">
    <div class="contact">
      <p>14 rue des Orvilles<br>Passage Marcellin<br>98 000 Monaco</p>
      <p class="phone">+377.93.48.25.71</p>
      <p class="web">www.brunor-agency.com</p>
    </div>
  </div>
</div>
</body>
</html>
```